Pfft... Caramel packaging

We want to create a derivative of our gummies packaging for our new product, our chewable caramel. We would like to use a caramel, brownish, cream pallet. With hints of green. See example1.pdf for an example of the colors, they DO NOT have to be exact. Check PFFT Dulce de Leche.psd for the logo with approximated colors, you can change these, but please keep logo structure. 3.62x4.50x1.50.pdf is the guideline for the packaging print, this includes size and print area. All Gummies Mock up.jpg is our gummies packaging line up, mocked up. All warnings must be included, use this as guide.

Designers are asking for more time, and i want higher quiality submissions.

```html
<!DOCTYPE html>
<html lang="en">
<head>
<meta charset="utf-8">
<title>Pfft... Caramel Chew – pouch print layout</title>
<link href="https://fonts.googleapis.com/css2?family=Roboto+Condensed:wght@400;700&family=Roboto:wght@700&display=swap" rel="stylesheet">
<style>
  :root{
    --bleed-green:#8dc63f;
    --band-cream:#f6e3a6;
    --dim-grey:#6f6f6f;
    --ink:#151515;
    --logo-ink:#3a3a3a;
    --leaf-green:#2f7d3a;
    --pill-green:#8fbf4a;
    --caramel:#f3a13a;
    --caramel-dark:#c86a1e;
    --chew-cream:#fbf3c8;
    --panel-white:#ffffff;
  }
  *{box-sizing:border-box;margin:0;padding:0}
  html,body{width:815px;height:1200px;overflow:hidden;background:#fff}
  body{position:relative;font-family:"Roboto Condensed",sans-serif;color:var(--ink)}
  .guides{position:absolute;inset:0}
  .abs{position:absolute}
  .dim-label{position:absolute;font-family:"Roboto",sans-serif;font-weight:700;color:var(--dim-grey);background:#fff;padding:0 4px;white-space:nowrap;line-height:1}
  .dim-label.big{font-size:16px}
  .dim-label.small{font-size:11px}
  .vertical{transform:translate(-50%,-50%) rotate(-90deg)}
  .vertical-down{transform:translate(-50%,-50%) rotate(90deg)}

  .wordmark{display:flex;align-items:center;gap:6px;color:var(--logo-ink);font-weight:700;line-height:1;white-space:nowrap}
  .wordmark .mark{border-radius:50%;background:var(--caramel-dark);flex:none}
  .front-logo{left:321px;top:326px;width:232px;height:67px;transform:rotate(-90deg);justify-content:center;font-size:50px}
  .front-logo .mark{width:40px;height:40px}
  .back-logo{left:460px;top:935px;width:206px;height:62px;transform:rotate(180deg);justify-content:center;font-size:48px}
  .back-logo .mark{width:38px;height:38px}

  .product-pill{position:absolute;border-radius:48px;border:3px solid #c9df8f;overflow:hidden}
  .pill-art{position:absolute;inset:0}
  .front-pill{left:487px;top:247px;width:89px;height:227px}
  .front-pill .pill-art{background:linear-gradient(180deg,#aacb63 0%,#8fbf4a 35%,var(--caramel) 50%,#e88a2c 75%,var(--leaf-green) 90%,#2d6e33 100%)}
  .back-pill{left:298px;top:936px;width:157px;height:60px;transform:rotate(180deg)}
  .back-pill .pill-art{background:linear-gradient(90deg,var(--leaf-green) 0%,#e88a2c 25%,var(--caramel) 50%,#8fbf4a 68%,#aacb63 100%)}
  .chew-badge{position:absolute;border-radius:50%;background:var(--chew-cream);border:3px solid #e7eeb0;display:flex;align-items:center;justify-content:center;text-align:center;font-weight:700;line-height:1.05;color:#222}
  .front-pill .chew-badge{left:3px;top:5px;width:78px;height:78px;font-size:16px}
  .back-pill .chew-badge{right:3px;top:3px;width:50px;height:50px;font-size:10px}

  .potency{position:absolute;left:355px;top:492px;width:140px;text-align:center}
  .potency .flavor{font-size:12.5px;line-height:15px}
  .potency .boxes{display:flex;margin:1px auto 0;width:120px;border:1.5px solid var(--ink)}
  .potency .boxes div{flex:1;font-size:13.5px;line-height:14px;padding:1px 0}
  .potency .boxes div+div{border-left:1.5px solid var(--ink)}
  .potency .type{font-size:12.5px;line-height:16px;margin-top:1px}
  .cert-badge{position:absolute;left:556px;top:496px;width:55px;height:55px;border-radius:50%;background:#111}

  .warning{position:absolute;left:290px;top:566px;width:380px;text-align:center;font-weight:700;font-size:12.5px;line-height:16px}

  .ingredients{position:absolute;width:182px;font-size:10.6px;line-height:13.2px;transform:rotate(180deg)}
  .ingredients b{font-weight:700}
  .ing-en{left:485px;top:655px;height:118px}
  .ing-es{left:485px;top:786px;height:140px}

  .nutrition{position:absolute;left:298px;top:655px;width:184px;height:264px;border:2px solid #000;padding:2px 3px;transform:rotate(180deg);font-family:"Roboto Condensed",sans-serif;color:#000}
  .nutrition h2{font-size:13.5px;line-height:13px;font-weight:700;letter-spacing:.3px}
  .nutrition .row{display:flex;justify-content:space-between;font-size:5.2px;line-height:9.4px;border-top:.6px solid #000}
  .nutrition .row.indent span:first-child{padding-left:6px}
  .nutrition .plain{font-size:5.4px;line-height:7px}
  .nutrition .bar{height:4px;background:#000;margin:1px 0}
  .nutrition .bar.mid{height:2px}
  .nutrition .cal{display:flex;justify-content:space-between;font-weight:700;font-size:11px;line-height:14px}
  .nutrition .cal span:last-child{font-size:13px}
  .nutrition .foot{font-size:4.2px;line-height:5.2px;margin-top:2px;border-top:.6px solid #000;padding-top:1px}
</style>
</head>
<body>

<svg class="guides" width="815" height="1200" viewBox="0 0 815 1200" aria-hidden="true">
  <defs>
    <marker id="arrow" viewBox="0 0 10 10" refX="9" refY="5" markerWidth="7" markerHeight="7" orient="auto-start-reverse">
      <path d="M0 1 L10 5 L0 9 Z" fill="var(--dim-grey)"/>
    </marker>
  </defs>

  <!-- bleed area -->
  <rect x="223" y="130" width="517" height="991" fill="var(--panel-white)"/>
  <rect x="528" y="130" width="212" height="991" fill="var(--band-cream)"/>
  <!-- seal margin tint -->
  <path d="M243 150 H719 V1101 H243 Z M293 200 V1051 H669 V200 Z" fill-rule="evenodd" fill="rgba(0,0,0,0.065)" stroke="#d6d6d6" stroke-width=".6"/>
  <rect x="223" y="130" width="517" height="991" fill="none" stroke="var(--bleed-green)" stroke-width="2"/>

  <!-- faint hang/seal arcs -->
  <g fill="none" stroke="#dedede" stroke-width="1.5">
    <path d="M243 507 A40 40 0 0 1 243 585"/>
    <path d="M243 665 A40 40 0 0 1 243 743"/>
    <path d="M719 507 A40 40 0 0 0 719 585"/>
    <path d="M719 665 A40 40 0 0 0 719 743"/>
  </g>

  <!-- centre fold -->
  <line x1="243" y1="625" x2="719" y2="625" stroke="#d8d8d8" stroke-width=".8"/>

  <!-- tear / fold lines -->
  <g stroke="#7a7a7a" stroke-width=".8" stroke-dasharray="5 4">
    <line x1="255" y1="237" x2="706" y2="237"/>
    <line x1="255" y1="1015" x2="706" y2="1015"/>
  </g>
  <g fill="#6a6a6a">
    <path d="M243 230 H255 L263 237 L255 244 H243 Z"/>
    <path d="M719 230 H707 L699 237 L707 244 H719 Z"/>
    <path d="M241 1008 H253 L261 1015 L253 1022 H241 Z"/>
    <path d="M717 1008 H705 L697 1015 L705 1022 H717 Z"/>
  </g>

  <!-- dimension extension lines -->
  <g stroke="#8a8a8a" stroke-width=".7">
    <line x1="243" y1="46" x2="243" y2="130"/>
    <line x1="719" y1="46" x2="719" y2="130"/>
    <line x1="293" y1="86" x2="293" y2="130"/>
    <line x1="669" y1="86" x2="669" y2="130"/>
    <line x1="80" y1="150" x2="223" y2="150"/>
    <line x1="80" y1="1101" x2="223" y2="1101"/>
    <line x1="140" y1="625" x2="223" y2="625"/>
    <line x1="736" y1="150" x2="782" y2="150"/>
    <line x1="700" y1="227" x2="782" y2="227"/>
  </g>

  <!-- dimension lines -->
  <g stroke="var(--dim-grey)" stroke-width="1" marker-start="url(#arrow)" marker-end="url(#arrow)">
    <line x1="244" y1="54" x2="718" y2="54"/>
    <line x1="244" y1="92" x2="292" y2="92"/>
    <line x1="294" y1="92" x2="668" y2="92"/>
    <line x1="670" y1="92" x2="718" y2="92"/>
    <line x1="91" y1="151" x2="91" y2="1100"/>
    <line x1="147" y1="151" x2="147" y2="624"/>
    <line x1="147" y1="626" x2="147" y2="1100"/>
    <line x1="773" y1="151" x2="773" y2="226"/>
  </g>
  <path d="M798 228 L815 212 V244 Z" fill="#6a6a6a"/>
</svg>

<!-- dimension labels -->
<span class="dim-label big" style="left:480px;top:54px;transform:translate(-50%,-50%)">3.00" [ 76.20mm ]</span>
<span class="dim-label small" style="left:268px;top:92px;transform:translate(-50%,-50%)">8mm</span>
<span class="dim-label big" style="left:481px;top:92px;transform:translate(-50%,-50%)">2.37" [ 60.20mm ]</span>
<span class="dim-label small" style="left:694px;top:92px;transform:translate(-50%,-50%)">8mm</span>
<span class="dim-label big vertical" style="left:91px;top:625px">6.00" [ 152.40mm ]</span>
<span class="dim-label big vertical" style="left:147px;top:388px">3.00" [ 76.20mm ]</span>
<span class="dim-label big vertical" style="left:147px;top:863px">3.00" [ 76.20mm ]</span>
<span class="dim-label big vertical-down" style="left:773px;top:188px">0.5in</span>

<!-- FRONT PANEL -->
<div class="wordmark front-logo abs"><span class="mark"></span><span>Pfft...</span></div>

<div class="product-pill front-pill">
  <div class="pill-art" role="img" aria-label="Illustration of stacked caramel chew cubes on a green background"></div>
  <div class="chew-badge">CARAMEL<br>CHEW</div>
</div>

<div class="potency">
  <div class="flavor">Caramel Favor</div>
  <div class="boxes"><div>10MG<br>Per Unit</div><div>100MG<br>Per Pack</div></div>
  <div class="type">Full Spectrum Gummies</div>
</div>
<div class="cert-badge" role="img" aria-label="Compliance badge"></div>

<p class="warning">Contains Medical Cannabis. This product complies with all mandatory contaminant testing.&nbsp; Keep out of reach of children.</p>

<!-- BACK PANEL (printed inverted) -->
<p class="ingredients ing-en"><b>Ingredients:</b> Brown sugar, condense milk (milk, sugar), glucose syrup (corn syrup, salt, vanilla extract (vanilla beans, water, ethyl alcohol), butter (pasteurized cream, natural flavoring), organic coconut oil, liquid sunflower lecithin, salt (sea salt, potassium iodide and yellow prussiate of soda (anticaking agent))</p>
<p class="ingredients ing-es"><b>Ingredientes:</b> Azúcar morena, leche condensada (leche azúcar), sirope de glucosa (sirope de maíz, sal, extracto de vainilla (vaina de vainilla, agua, alcohol etílico), mantequilla (crema pasteurizada, sabores naturales), aceite de coco orgánico, lecitina de girasol líquida, sal (sal marina, yoduro de potasio y prusiato de amarillo de soda (para evitar endurecimiento))</p>

<div class="nutrition">
  <h2>Datos de Nutrición<br>Nutrition Facts</h2>
  <div class="plain">2 Raciones por Envase / 2 servings per container</div>
  <div class="plain" style="display:flex;justify-content:space-between;font-weight:700;font-size:6px"><span>Ración / Serv. size</span><span>1 pieza (5g) / 1 piece (5g)</span></div>
  <div class="bar"></div>
  <div class="plain">Cantidad por ración / Amount per serving</div>
  <div class="cal"><span>Calorías / Calories</span><span>25</span></div>
  <div class="bar mid"></div>
  <div class="plain" style="text-align:right">% Valor Diario* / % Daily Value*</div>
  <div class="row"><span>Grasa Total / Total Fat 1g</span><span>1%</span></div>
  <div class="row indent"><span>Grasa Sat. / Sat. Fat 0.5g</span><span>3%</span></div>
  <div class="row indent"><span>Grasa Trans / Trans Fat 0g</span><span></span></div>
  <div class="row"><span>Colest. / Cholest. 5mg</span><span>2%</span></div>
  <div class="row"><span>Sodio / Sodium 10mg</span><span>0%</span></div>
  <div class="row"><span>Carb. Total / Total Carb. 4g</span><span>1%</span></div>
  <div class="row indent"><span>Fibra / Fiber 0g</span><span>0%</span></div>
  <div class="row indent"><span>Azúcares Totales / Total Sugars 4g</span><span></span></div>
  <div class="row indent"><span>Incluye 3g Azúcares Añadidos / Includes 3g Added Sugars</span><span>6%</span></div>
  <div class="row"><span>Proteínas / Protein 0g</span><span></span></div>
  <div class="bar"></div>
  <div class="row"><span>Vit. D 0mcg</span><span>0%</span></div>
  <div class="row"><span>Calcio / Calcium 6mg</span><span>0%</span></div>
  <div class="row"><span>Hierro / Iron 0mg</span><span>0%</span></div>
  <div class="row"><span>Potas. 7mg</span><span>0%</span></div>
  <div class="foot">*El % Valor Diario (VD) le indica cuanto un nutriente en una porción de alimentos contribuye a una dieta diaria. *The % Daily Value tells you how much a nutrient in a serving of food contributes to a daily diet. 2,000 calories a day is used for general nutrition advice.</div>
</div>

<div class="product-pill back-pill">
  <div class="pill-art" role="img" aria-label="Illustration of stacked caramel chew cubes on a green background"></div>
  <div class="chew-badge">CARAMEL<br>CHEW</div>
</div>

<div class="wordmark back-logo abs"><span class="mark"></span><span>Pfft...</span></div>

</body>
</html>
```